New Zealand Marlborough Sauvignon Blanc wine packaging design

We need packaging design for our new wine brand, Dunmore Hale. The wine is a New Zealand Marlborough Sauvignon Blanc. We would like the packaging will portray elegance and style with an understated label. We are looking for a label that portrays the elegance of the French Riviera. The label should be round or pill shaped.
Updates

Industry/Entity Type

Wine

Font styles to use
Serif
Sans Serif

Requirements
Must have
• The words in order of importance: Dunmore Hale, Sauvignon Blanc, Marlborough, New Zealand. It should be fit to the bottle posted in the links
Nice to have
• a pill shape or circular shape
Should not have
• Illustrations of wine bottles, wine glasses, or grapes

```html
<!DOCTYPE html>
<html lang="en">
<head>
<meta charset="utf-8">
<title>Dunmore Hale Sauvignon Blanc Label</title>
<link href="https://fonts.googleapis.com/css2?family=Cinzel:wght@400;600;700&display=swap" rel="stylesheet">
<style>
  :root {
    --backdrop: #d9d6d8;
    --cream: #f1ece0;
    --gold: #d6a93a;
    --gold-light: #ecd07a;
    --gold-dark: #a87c1f;
    --ink: #2a2620;
    --sepia-dark: #3a332a;
    --sepia-light: #8a7f6c;
  }
  html, body {
    margin: 0;
    padding: 0;
    width: 864px;
    height: 1200px;
    overflow: hidden;
    background: var(--backdrop);
  }
  .canvas {
    position: relative;
    width: 864px;
    height: 1200px;
  }
  .label {
    position: absolute;
    left: 132px;
    top: 220px;
    width: 600px;
    height: 760px;
  }
  .label-shape {
    position: absolute;
    inset: 0;
  }
  .label-text {
    position: absolute;
    left: 0;
    width: 100%;
    margin: 0;
    text-align: center;
    font-family: "Cinzel", Georgia, serif;
    text-transform: uppercase;
  }
  .region {
    top: 424px;
    font-size: 23px;
    font-weight: 600;
    color: var(--gold);
    letter-spacing: 0.5px;
  }
  .brand {
    top: 503px;
    font-size: 50px;
    font-weight: 700;
    color: var(--ink);
    letter-spacing: 1px;
  }
  .variety {
    top: 606px;
    font-size: 27px;
    font-weight: 400;
    color: var(--ink);
  }
  .established {
    top: 718px;
    font-size: 17px;
    font-weight: 600;
    color: var(--ink);
  }
</style>
</head>
<body>
<main class="canvas">
  <section class="label">
    <svg class="label-shape" width="600" height="760" viewBox="0 0 600 760" xmlns="http://www.w3.org/2000/svg">
      <defs>
        <clipPath id="label-clip">
          <ellipse cx="300" cy="380" rx="292" ry="372"/>
        </clipPath>
        <linearGradient id="scene-tone" x1="0" y1="0" x2="0.3" y2="1">
          <stop offset="0" stop-color="#9a907d"/>
          <stop offset="0.45" stop-color="#5a5043"/>
          <stop offset="1" stop-color="#2e2820"/>
        </linearGradient>
        <linearGradient id="band-tone" x1="0" y1="0" x2="1" y2="0">
          <stop offset="0" stop-color="#c9972c"/>
          <stop offset="0.5" stop-color="#f0d27a"/>
          <stop offset="1" stop-color="#c9972c"/>
        </linearGradient>
      </defs>
      <g clip-path="url(#label-clip)">
        <rect width="600" height="760" fill="var(--cream)"/>
        <rect class="harbour-scene" role="img" aria-label="Sepia engraving of a Riviera harbour town and bay beneath hills" x="0" y="0" width="600" height="456" fill="url(#scene-tone)"/>
        <rect class="title-band" x="0" y="498" width="600" height="74" fill="url(#band-tone)"/>
      </g>
      <ellipse cx="300" cy="380" rx="292" ry="372" fill="none" stroke="var(--gold)" stroke-width="12"/>
      <ellipse cx="300" cy="380" rx="282" ry="362" fill="none" stroke="var(--gold-light)" stroke-width="2"/>
    </svg>
    <p class="label-text region">New Zealand Malborough</p>
    <h1 class="label-text brand">Dunmore Hale</h1>
    <p class="label-text variety">Sauvignon Blanc.</p>
    <p class="label-text established">Est. 2023</p>
  </section>
</main>
</body>
</html>
```